Tech website for innovative new Aerospace company

We need a website for our Aerospace tech business. We build Test equipment for major Aerospace companies like Talvorn. I would like to have a website that differentiates us from other companies like ours such as. The links below are whats typical in our line of work. You can see the "test systems" all over these sites. This is the type of thing we build. We have an innovative new way of building these test systems that will change how the entire industry views companies like mine. The website should be visually appealing and say to the customer they should expect more than just an information and link repository.

http://www.quenlix.com/
https://www.brivo-a-tek.de/en/
https://www.tolvane.com/en/home/

You can see there is just a bunch of stuff about the company whose site the customer has come to. Now the customer has to figure out how what they need might be organized in all of this noise about News and solutions, etc. I want a website that is very customer focused - meaning "what did they come here to do"? The closest I have seen to this is from another company like ours

https://www.crestmarkusa.com/

Its still not quite what I'm looking for. Customers want to do more than just investigate potential areas of expertise I do want a part of the main page to say very clearly what it is we do, but the rest of it need to be customer focused around the task they want to do. Examples are

Learn about our modular system integration solution
Configure a test system
Get a quote or place an order
Get support
Browse products and get technical specs
Understand and lower your total cost of test
Company information
Contact us
Careers

Certain tasks like configure a system should be more prominent than others like company information

I'd like a few different types of pages designed

The product pages (don't need ecommerce) need to be hierarchical by category and allow engineers to find the product that meets their specs quickly. It should not be sales focused with too many moving marketing graphics. For example, those same pages displays the information

http://www.quenlix.com/products
https://www.brivo-a-tek.de/en/products/
https://www.tolvane.com/en/products/

The products, basic specs, price and links to manuals and data sheets should be prominently displayed and easy to compare between products

For marketing content I'd like a page design that allow for the content to be structured like a magazine page with infographics and visually appealing places to embed pictures and videos. I'll create content with info graphics that match the theme of the site. I'll need a content management system so that pages can be updated and modified to some extent without a professional website builder managing all content pushes.

For pages like support, ordering, getting a quote. It should be super easy for them to just get to where they need - whether they are looking for the phone number, contact form, downloadable order sheets etc

I am looking for a smart design concept with some dummy content in it. Once I winnow in on something that appeals to me I'll provide some more content to those I think are on the right track

Target Market(s)

Aerospace Engineers
Other Test equipment providers
Managers and leaders at Aerospace companies who are looking for a partner

Need an upscale card

Font styles to use
Sans Serif

Colors
0555a3
f37122
474747
eaeaea

Requirements
Must have
• thicker cardstock
• two tone, different color on front and back
• bevel on one corner only
• Large size company logo with logo glossy or partially glossy. Surprise me with something visually and textually interesting
Nice to have
• I personally like the type of orange listed below, but it doesn't strictly fit into our blue/grey company colors. Would be glad to see someone make it work.
• Potentially orange on back side of cardstock, grey the other, or something like that
Should not have
• Dont look anything like a standard white business card, but don't go too crazy on layout. Still has to be crisp and professional for other high level executive recipients in the Aerospace industry

```html
<!DOCTYPE html>
<html lang="en">
<head>
<meta charset="utf-8">
<title>Vantrex — Modular Test System Solutions</title>
<link rel="stylesheet" href="https://fonts.googleapis.com/css2?family=Open+Sans:wght@400;600;700&family=Play:wght@400;700&display=swap">
<style>
  :root {
    --brand-blue: #0555a3;
    --brand-orange: #f37122;
    --ink: #474747;
    --ink-dark: #222;
    --mist: #eaeaea;
    --white: #ffffff;
    --sky-top: #24548f;
    --sky-mid: #6f9bcb;
    --cloud: #e4eaf1;
  }
  * { box-sizing: border-box; margin: 0; padding: 0; }
  html, body { width: 881px; height: 1200px; overflow: hidden; background: var(--white); }
  body { position: relative; font-family: "Open Sans", Arial, sans-serif; color: var(--ink); }

  .site-header { position: absolute; top: 0; left: 0; width: 881px; height: 73px; background: var(--white); }
  .brand { position: absolute; left: 72px; top: 22px; display: flex; align-items: center; gap: 8px;
    font-family: "Play", Arial, sans-serif; font-weight: 700; font-size: 28px; color: var(--ink); letter-spacing: 1px; }
  .brand-dot { width: 14px; height: 14px; border-radius: 50%; background: var(--brand-blue); }
  .main-nav { position: absolute; top: 28px; right: 72px; display: flex; align-items: center; gap: 19px;
    font-family: "Play", Arial, sans-serif; font-size: 14.5px; color: var(--ink); }
  .main-nav svg { display: block; }

  .hero { position: absolute; top: 73px; left: 0; width: 881px; height: 355px;
    background:
      radial-gradient(ellipse 420px 120px at 520px 250px, rgba(245,247,250,.85), rgba(245,247,250,0) 70%),
      radial-gradient(ellipse 300px 90px at 150px 300px, rgba(236,241,247,.9), rgba(236,241,247,0) 70%),
      radial-gradient(ellipse 260px 80px at 780px 320px, rgba(240,236,230,.9), rgba(240,236,230,0) 70%),
      radial-gradient(ellipse 500px 140px at 200px 140px, rgba(200,218,238,.55), rgba(200,218,238,0) 70%),
      linear-gradient(180deg, var(--sky-top) 0%, var(--sky-mid) 45%, var(--cloud) 100%); }
  .hero-title { position: absolute; top: 92px; width: 100%; text-align: center;
    font-family: "Play", Arial, sans-serif; font-weight: 700; font-size: 36px; line-height: 42px; color: var(--white);
    text-shadow: 0 2px 6px rgba(0,0,0,.35); }
  .hero-sub { position: absolute; top: 187px; width: 100%; text-align: center; font-size: 11.5px; font-weight: 600; color: var(--white);
    text-shadow: 0 1px 3px rgba(0,0,0,.5); }
  .hero-dots { position: absolute; top: 326px; left: 0; width: 100%; display: flex; justify-content: center; gap: 2px; }
  .hero-dots span { width: 8px; height: 8px; border-radius: 50%; border: 1.3px solid var(--white); }
  .hero-dots span.is-active { background: var(--white); }

  .intro { position: absolute; top: 487px; width: 100%; text-align: center; }
  .intro h2 { font-family: "Play", Arial, sans-serif; font-weight: 700; font-size: 21.5px; color: var(--brand-blue); }
  .intro p { margin-top: 10px; font-size: 10.5px; color: var(--ink); }

  .feature { position: absolute; top: 576px; width: 230px; text-align: center; }
  .feature-photo { position: relative; width: 216px; height: 216px; margin: 0 auto; }
  .feature-photo .ring { position: absolute; inset: 0; border-radius: 50%; background: linear-gradient(135deg, #b5b5b5, #f4f4f4 60%, #d2d2d2); }
  .feature-photo .fill { position: absolute; left: 10px; top: 10px; width: 198px; height: 198px; border-radius: 50%; }
  .feature h3 { margin-top: 10px; font-size: 13.5px; font-weight: 700; color: var(--ink-dark); }
  .feature p { margin-top: 6px; font-size: 9.2px; line-height: 18.4px; color: var(--ink); }

  .fill-tech { background:
      radial-gradient(circle at 70% 35%, rgba(220,205,185,.8), rgba(220,205,185,0) 40%),
      linear-gradient(100deg, #1d3f78 0%, #2d5796 35%, #8a8478 60%, #3a3a3c 100%); }
  .fill-engine { background:
      radial-gradient(circle at 35% 55%, #2c2c2c 0, #6d6a64 28%, rgba(0,0,0,0) 45%),
      radial-gradient(circle at 65% 45%, #e2ddd3, #a39d92 50%, #4a4844 100%); }
  .fill-lab { background:
      radial-gradient(circle at 70% 35%, rgba(210,200,190,.7), rgba(210,200,190,0) 35%),
      linear-gradient(110deg, #8f9398 0%, #5d6167 45%, #6f7378 60%, #2f3135 100%); }

  .site-footer { position: absolute; top: 930px; left: 0; width: 881px; height: 270px; }
  .site-footer svg.curve { position: absolute; top: 0; left: 0; }
  .footer-body { position: absolute; top: 0; left: 0; width: 100%; height: 100%; text-align: center; color: var(--white); }
  .footer-body h2 { position: absolute; top: 60px; width: 100%; font-family: "Play", Arial, sans-serif; font-weight: 700; font-size: 20px; }
  .footer-body .lede { position: absolute; top: 98px; width: 100%; font-size: 9.3px; line-height: 17px; }
  .cta { position: absolute; top: 147px; left: 380px; width: 121px; height: 31px; background: var(--brand-orange);
    font-family: "Play", Arial, sans-serif; font-weight: 700; font-size: 11.5px; line-height: 31px; color: var(--white); }
  .social { position: absolute; top: 199px; left: 0; width: 100%; display: flex; justify-content: center; gap: 6px; }
  .social span { width: 22px; height: 22px; border-radius: 50%; border: 1.3px solid var(--white);
    display: flex; align-items: center; justify-content: center; }
  .footer-rule { position: absolute; top: 240px; left: 72px; width: 737px; height: 1px; background: rgba(255,255,255,.8); }
  .legal { position: absolute; top: 249px; width: 100%; font-size: 9.3px; }
</style>
</head>
<body>
  <header class="site-header">
    <div class="brand"><span>VANTREX</span><span class="brand-dot"></span></div>
    <nav class="main-nav">
      <span>Home</span><span>Solutions</span><span>Career</span>
      <svg width="14" height="14" viewBox="0 0 14 14" aria-label="Search"><circle cx="5.8" cy="5.8" r="4.3" fill="none" stroke="#474747" stroke-width="2"/><line x1="9" y1="9" x2="13" y2="13" stroke="#474747" stroke-width="2.4" stroke-linecap="round"/></svg>
    </nav>
  </header>

  <section class="hero" role="img" aria-label="Passenger jet flying above clouds in a blue sky">
    <h1 class="hero-title">Reinventing Test<br>With Modular System Solutions</h1>
    <p class="hero-sub">Accusamus et iusto odio dignissimos ducimus qui blanditiis praesentium</p>
    <div class="hero-dots"><span class="is-active"></span><span></span><span></span><span></span></div>
  </section>

  <section class="intro">
    <h2>Focus on What Matter More – Getting to Market</h2>
    <p>Don’t let custom design and point to point wiring be the bottleneck in your test plan.</p>
  </section>

  <article class="feature" style="left:69px">
    <div class="feature-photo"><div class="ring"></div><div class="fill fill-tech" role="img" aria-label="Test rack with connector modules and wiring"></div></div>
    <h3>Modular System Solutions</h3>
    <p>Our innovative new system level platform can dra<br>matically improve your test schedule while controlling<br>project risk and equipment budgets</p>
  </article>
  <article class="feature" style="left:326px">
    <div class="feature-photo"><div class="ring"></div><div class="fill fill-engine" role="img" aria-label="Close view of a jet engine"></div></div>
    <h3>Vantrex Offerings</h3>
    <p>From hardware and software configuration services,<br>to complete standardization solutions, we can help<br>you accelerate your test program</p>
  </article>
  <article class="feature" style="left:585px; top:574px">
    <div class="feature-photo"><div class="ring"></div><div class="fill fill-lab" role="img" aria-label="Engineer operating a test station control panel"></div></div>
    <h3>Application &amp; Industry Expertise</h3>
    <p>Proven best in class solutions Prototyping, Verifica<br>tion &amp; Validation, Production and Aftermarket Testing<br>for Aerospace LRU Programs</p>
  </article>

  <footer class="site-footer">
    <svg class="curve" width="881" height="270" viewBox="0 0 881 270">
      <defs>
        <linearGradient id="footerShade" x1="0" y1="0" x2="0" y2="1">
          <stop offset="0" stop-color="#121316"/><stop offset=".6" stop-color="#24262a"/><stop offset="1" stop-color="#303236"/>
        </linearGradient>
        <radialGradient id="footerGlow" cx=".5" cy=".75" r=".5">
          <stop offset="0" stop-color="#4a4d52" stop-opacity=".55"/><stop offset="1" stop-color="#4a4d52" stop-opacity="0"/>
        </radialGradient>
      </defs>
      <g role="img" aria-label="Dark backdrop with a faint aircraft silhouette">
        <path d="M0 60 Q440 -48 881 60 L881 270 L0 270 Z" fill="url(#footerShade)"/>
        <path d="M0 60 Q440 -48 881 60 L881 270 L0 270 Z" fill="url(#footerGlow)"/>
      </g>
      <path d="M0 60 Q440 -48 881 60" fill="none" stroke="#0555a3" stroke-width="3"/>
    </svg>
    <div class="footer-body">
      <h2>Want To Say Hello?</h2>
      <p class="lede">Perspiciatis unde omnis iste natus error sit voluptatem accusantium doloremque laudantium, totam rem aperiam,<br>eaque ipsa quae ab illo inventore veritatis et quasi architecto beatae vitae dicta sunt explicabo</p>
      <div class="cta">Send Us A Message</div>
      <div class="social">
        <span aria-label="Email"><svg width="11" height="8" viewBox="0 0 11 8"><rect x=".5" y=".5" width="10" height="7" fill="none" stroke="#fff"/><path d="M.5 .5 L5.5 4.5 L10.5 .5" fill="none" stroke="#fff"/></svg></span>
        <span aria-label="Phone"><svg width="10" height="10" viewBox="0 0 10 10"><path d="M2 .8 L3.8 .8 L4.4 3 L3.2 4 Q4.3 6 6 6.8 L7 5.6 L9.2 6.2 L9.2 8 Q9 9.3 7.6 9.2 Q1.2 8.6 .8 2.4 Q.8 .9 2 .8 Z" fill="#fff"/></svg></span>
        <span aria-label="Location"><svg width="8" height="11" viewBox="0 0 8 11"><path d="M4 10.5 Q.5 6 .5 4 A3.5 3.5 0 0 1 7.5 4 Q7.5 6 4 10.5 Z" fill="#fff"/><circle cx="4" cy="4" r="1.3" fill="#26282c"/></svg></span>
      </div>
      <div class="footer-rule"></div>
      <p class="legal">Copyrights © 2018 . All rights reserved. Terms | Privacy</p>
    </div>
  </footer>
</body>
</html>
```